We need a business card design for a Dubai based company .

We need a business card for a Dubai based company called "Zernova Smoking Requisites Trading LLC". We mainly import Flavoured Tobacco products and Charcoal which is used for smoking in a Hookah/Shisha and distribute to the wholesalers and retailers. Logo file is attached herewith.

```html
<!DOCTYPE html>
<html lang="en">
<head>
<meta charset="utf-8">
<title>Zernova Smoking Requisites Trading LLC – Business Card</title>
<link href="https://fonts.googleapis.com/css2?family=Arimo:wght@400;700&display=swap" rel="stylesheet">
<style>
  :root {
    --backdrop: #2b2b2b;
    --card: #222222;
    --ink: #f2f2f2;
    --ink-soft: #d6d6d6;
    --accent: #c8282b;
  }
  * { box-sizing: border-box; margin: 0; padding: 0; }
  html, body {
    width: 1200px; height: 900px; overflow: hidden;
    background: var(--backdrop);
    font-family: "Arimo", Arial, sans-serif;
    color: var(--ink);
  }
  .stage {
    width: 1200px; height: 900px;
    display: flex; flex-direction: column;
    align-items: center; justify-content: center; gap: 48px;
  }
  .card {
    position: relative;
    width: 630px; height: 360px;
    background: var(--card);
    box-shadow: 0 18px 40px rgba(0,0,0,0.45);
  }
  /* Contact side */
  .contact-side .person { position: absolute; left: 60px; top: 120px; }
  .person-name { font-size: 22px; font-weight: 700; }
  .person-role { font-size: 16px; color: var(--ink-soft); margin-top: 2px; }
  .contact-list { position: absolute; left: 60px; top: 196px; list-style: none; }
  .contact-list li { display: flex; align-items: center; gap: 10px; font-size: 16px; line-height: 24px; }
  .contact-list svg { width: 16px; height: 16px; flex: none; }
  .address { position: absolute; left: 60px; top: 262px; font-size: 16px; line-height: 21px; font-style: normal; }
  .brand-block {
    position: absolute; right: 60px; top: 70px;
    display: flex; align-items: center; gap: 12px;
  }
  .brand-mark { width: 14px; height: 14px; background: var(--accent); }
  .brand-name { font-size: 34px; font-weight: 400; letter-spacing: 4px; text-transform: uppercase; color: var(--ink); }
  .brand-tagline {
    position: absolute; right: 60px; top: 122px;
    font-size: 10px; letter-spacing: 2px; text-transform: uppercase; color: var(--accent);
  }
  .website { position: absolute; right: 55px; bottom: 50px; font-size: 15px; letter-spacing: 1px; }
  .accent-band { position: absolute; right: 55px; bottom: 28px; width: 180px; height: 12px; background: var(--accent); }
  /* Brand side */
  .brand-side { display: flex; flex-direction: column; align-items: center; justify-content: center; gap: 14px; }
  .brand-side .brand-name { font-size: 54px; letter-spacing: 8px; color: #8f8f8f; }
  .brand-side .brand-tagline { position: static; font-size: 13px; letter-spacing: 4px; }
</style>
</head>
<body>
<main class="stage">
  <section class="card contact-side" aria-label="Business card, contact side">
    <div class="person">
      <p class="person-name">Rahul Mehta</p>
      <p class="person-role">Sales Manager</p>
    </div>
    <ul class="contact-list">
      <li>
        <svg viewBox="0 0 16 16" aria-hidden="true"><path d="M4 1.5l2.2 3-1.4 1.6c.8 1.9 2.2 3.4 4.1 4.3l1.6-1.4 3 2.2-1.3 2.6C7.4 13.6 2.4 8.6 1.4 3.8z" fill="var(--accent)"/></svg>
        <span>123.555.0142</span>
      </li>
      <li>
        <svg viewBox="0 0 16 16" aria-hidden="true"><rect x="1.5" y="3.5" width="13" height="9" fill="none" stroke="var(--accent)" stroke-width="1.4"/><path d="M1.5 3.5L8 9l6.5-5.5M1.5 12.5L6 8M14.5 12.5L10 8" fill="none" stroke="var(--accent)" stroke-width="1.2"/></svg>
        <span>mehta@zernova.com</span>
      </li>
    </ul>
    <address class="address">Unit KR 0X<br>Oasis Trade Hub Int. City<br>Dubai AE</address>
    <div class="brand-block">
      <span class="brand-mark" aria-hidden="true"></span>
      <span class="brand-name">Zernova</span>
    </div>
    <p class="brand-tagline">Smoking Requisites Trading LLC</p>
    <p class="website">www.zernova.com</p>
    <div class="accent-band" aria-hidden="true"></div>
  </section>

  <section class="card brand-side" aria-label="Business card, brand side">
    <span class="brand-name">Zernova</span>
    <p class="brand-tagline">Smoking Requisites Trading LLC</p>
  </section>
</main>
</body>
</html>
```